Residential improvers, A Cozy Perch 2 Go *

Cozy Perch 2 Go is a real estate company specializing in turning unloved properties into improved, happy places to live. We specialize in thoughtfully-improved residential properties for buyers or renters. Our company needs a business card that reflects the renovated homes we create using green and Feng Shui principles,

Please disregard the images we submitted. We are looking for an abstract, sophisticated elegant design. No eggs in a nest ... nothing cute. The image can be soft.
Updates

Aloha (hello) all designers. We are a serious property investment/improvement company. We strive to be unique, renovating with style and elegance. Our business card must portray the same message. We thought the nest and flower might be "it" ... clearly it's not, once we saw what you submitted. Please revisit the brief as it was modified yesterday. Mahalo for your input! We look forward to hearing from all designers that have been invited.

Industry/Entity Type

Real Estate Development

Contact Information for Business Card

We will have separate business cards for
1) Corabeth Lindqvist 808-555-0173 corabeth@mailbrook.test
2) Marla Fenwright 808-555-0198 marlafenwright@mailbrook.test
** can we add the website later ... in the process of approval.
Investors * Renovators * Connectors

Font styles to use
Sans Serif

Colors
cadf82

Requirements
Must have
• a feng shui feel ... modern. Color - green with black print.
Nice to have
• A Cozy Perch 2 Go

```html
<!DOCTYPE html>
<html lang="en">
<head>
<meta charset="utf-8">
<title>A Cozy Perch 2 Go — Business Card</title>
<link rel="stylesheet" href="https://fonts.googleapis.com/css2?family=Montserrat:wght@400;500&family=Great+Vibes&display=swap">
<style>
  :root {
    --page-bg: #2b2b2b;
    --card-green: #cadf82;
    --card-light: #e4efbb;
    --card-white: #ffffff;
    --ink: #1c1f14;
    --mark-green: #6a8a2a;
  }
  * { box-sizing: border-box; margin: 0; padding: 0; }
  html, body {
    width: 1200px; height: 906px; overflow: hidden;
    background: var(--page-bg);
  }
  .canvas {
    position: relative; width: 1200px; height: 906px;
    display: flex; flex-direction: column; align-items: center;
    justify-content: space-evenly;
  }
  .card {
    position: relative; width: 660px; height: 377px;
    border-radius: 28px; overflow: hidden;
    font-family: "Montserrat", sans-serif; color: var(--ink);
  }
  .card--front {
    background: radial-gradient(ellipse 42% 62% at 50% 48%, var(--card-white) 0%, var(--card-light) 55%, var(--card-green) 100%);
  }
  .card--back {
    background: radial-gradient(ellipse 40% 60% at 70% 40%, var(--card-white) 0%, var(--card-light) 50%, var(--card-green) 100%);
  }
  .brand {
    position: absolute; display: flex; flex-direction: column; align-items: center;
  }
  .card--front .brand { left: 0; right: 0; top: 118px; }
  .card--back .brand { left: 330px; width: 300px; top: 104px; }
  .brand__row { display: flex; align-items: center; gap: 12px; }
  .brand__dot {
    width: 22px; height: 22px; border-radius: 50%; background: var(--mark-green);
  }
  .brand__name {
    font-weight: 500; font-size: 30px; letter-spacing: 0.5px; color: var(--ink);
    white-space: nowrap;
  }
  .brand__tagline {
    margin-top: 12px; font-size: 14px; letter-spacing: 0.4px; color: var(--ink);
    white-space: nowrap;
  }
  .card--back .brand__name { font-size: 26px; }
  .card--back .brand__tagline { font-size: 13px; }
  .person-name {
    position: absolute; left: 40px; top: 40px;
    font-family: "Great Vibes", cursive; font-size: 46px; color: var(--ink);
  }
  .contact-list {
    position: absolute; left: 44px; bottom: 42px;
    list-style: none; display: flex; flex-direction: column; gap: 8px;
  }
  .contact-list li {
    display: flex; align-items: center; gap: 12px; font-size: 16px; font-weight: 500;
  }
  .contact-list svg { width: 16px; height: 16px; fill: var(--ink); flex: none; }
</style>
</head>
<body>
<main class="canvas">
  <section class="card card--front" aria-label="Card front">
    <div class="brand">
      <div class="brand__row">
        <span class="brand__dot"></span>
        <span class="brand__name">A Cozy Perch 2 Go</span>
      </div>
      <p class="brand__tagline">Investors • Renovators • Connectors</p>
    </div>
  </section>

  <section class="card card--back" aria-label="Card back">
    <p class="person-name">Corabeth Lindqvist</p>
    <div class="brand">
      <div class="brand__row">
        <span class="brand__dot"></span>
        <span class="brand__name">A Cozy Perch 2 Go</span>
      </div>
      <p class="brand__tagline">Investors • Renovators • Connectors</p>
    </div>
    <ul class="contact-list">
      <li>
        <svg viewBox="0 0 24 24" aria-hidden="true"><path d="M6.6 10.8a15.1 15.1 0 0 0 6.6 6.6l2.2-2.2c.3-.3.7-.4 1-.2 1.1.4 2.3.6 3.6.6.6 0 1 .4 1 1V20c0 .6-.4 1-1 1A17 17 0 0 1 3 4c0-.6.4-1 1-1h3.5c.6 0 1 .4 1 1 0 1.3.2 2.5.6 3.6.1.3 0 .7-.2 1z"/></svg>
        <span>808-555-0173</span>
      </li>
      <li>
        <svg viewBox="0 0 24 24" aria-hidden="true"><path d="M2 5h20v14H2z M2 5l10 8 10-8" fill="none" stroke="#1c1f14" stroke-width="2"/></svg>
        <span>corabeth@mailbrook.test</span>
      </li>
      <li>
        <svg viewBox="0 0 24 24" aria-hidden="true"><g fill="none" stroke="#1c1f14" stroke-width="1.8"><circle cx="12" cy="12" r="9.5"/><ellipse cx="12" cy="12" rx="4" ry="9.5"/><path d="M2.5 12h19M4 7h16M4 17h16"/></g></svg>
        <span>acozyperch2go.test</span>
      </li>
    </ul>
  </section>
</main>
</body>
</html>
```